Modernization of our corporate website

The goal of this task is to propose a new template for our website, http://vlomik.example/

We just made a new batch of business cards (see attachments) and the new website has to match them.

Feel free to request current HTML.

Industry/Entity Type

Business

```html
<!DOCTYPE html>
<html lang="en">
<head>
<meta charset="utf-8">
<title>Vlomik — Hosting</title>
<link href="https://fonts.googleapis.com/css2?family=Marcellus&family=PT+Sans:wght@400;700&family=PT+Sans+Narrow:wght@400;700&family=Noto+Serif:ital,wght@0,400;1,400&display=swap" rel="stylesheet">
<style>
:root{
  --sky-top:#2f86a8;--sky-bottom:#1b5676;--navy:#0f2a45;--navy-dark:#13283c;
  --panel:#ffffff;--green:#86b21b;--green-dark:#6a9410;--green-active:#4f7a0a;
  --hero-light:#aacb3f;--hero-dark:#86b02a;--orange:#f5a52a;--orange-dark:#e07f12;
  --read-more:#e8802a;--ink:#1c3d5c;--body-text:#666;--dark-text:#444;
  --cream:#efe7c9;--red:#c23b1e;--blue:#0b5aa8;--card:#ececec;--footer-text:#c4d2de;
}
*{box-sizing:border-box;margin:0;padding:0}
html,body{width:1145px;height:1200px;overflow:hidden}
body{background:var(--navy);font-family:"PT Sans",sans-serif}
.page{position:relative;width:1050px;height:1100px;transform:scale(1.0905,1.0909);transform-origin:0 0;
  background:linear-gradient(180deg,var(--sky-top) 0,var(--sky-bottom) 145px,var(--navy) 146px)}
.abs{position:absolute}
.logo{left:60px;top:12px;font-family:"Marcellus",serif;font-size:52px;color:var(--cream)}
.top-links{left:632px;top:34px;color:#fff;font-size:12.5px;display:flex;gap:14px}
.search{left:815px;top:27px;width:173px;height:28px;border-radius:14px;background:#fff;border:1px solid #9cc;font-size:11px;font-style:italic;color:#aaa;padding:6px 14px}
.search svg{position:absolute;right:10px;top:7px}
.panel{left:45px;top:87px;width:960px;height:932px;background:var(--panel);border-radius:3px}
.nav{left:51px;top:92px;width:950px;height:50px;display:flex;background:linear-gradient(var(--green),var(--green-dark))}
.nav a{display:flex;align-items:center;justify-content:center;color:#fff;font-size:13.5px;text-decoration:none;border-right:1px solid rgba(0,0,0,.15);gap:8px}
.nav a.active{background:var(--green-active)}
.hero{left:54px;top:163px;width:950px;height:208px;background:radial-gradient(circle at 40% 40%,var(--hero-light),var(--hero-dark))}
.hero-title{left:116px;top:191px;color:#fff;font-size:23px;font-weight:700}
.badge{left:129px;top:250px;width:80px;height:80px;border-radius:50%;background:radial-gradient(#5a5358,#231f22);border:2px solid #fff;color:#fff;text-align:center;transform:rotate(-12deg);padding-top:18px;font-size:13px;line-height:1.1}
.badge b{font-size:18px;display:block}
.bullets{left:234px;top:243px;list-style:none;color:#fff;font-size:12.5px}
.bullets li{height:24px}
.bullets li::before{content:"";display:inline-block;border:4px solid transparent;border-left:5px solid #fff;margin-right:9px}
.btn{top:280px;width:91px;height:29px;border-radius:3px;background:linear-gradient(var(--orange),var(--orange-dark));color:#6a3a06;font-size:12px;font-weight:700;display:flex;align-items:center;justify-content:center}
.servers{left:755px;top:163px;width:245px;height:250px;background:linear-gradient(90deg,#2b2b2b,#4a4a4a 50%,#1a1a1a)}
.plan{top:395px;width:186px;text-align:center}
.plan h2{font-family:"PT Sans Narrow",sans-serif;font-size:20px;color:#2a4a6a;text-shadow:0 1px 1px #aaa;height:32px}
.plan .card{position:relative;height:292px;background:var(--card)}
.plan svg{position:absolute;left:42px;top:0}
.price{position:absolute;left:42px;top:12px;width:104px;color:#fff;font-family:"Noto Serif",serif;font-size:22px;line-height:1}
.price i{display:block;font-size:13px;margin-top:4px}
.plan ul{position:absolute;left:18px;top:86px;width:150px;list-style:none;font-size:11.5px;color:var(--dark-text)}
.plan li{height:28px;line-height:28px;border-top:1px dashed #bbb}
.plan li:first-child{border-top:none}
.plan .more{position:absolute;left:0;bottom:0;width:186px;height:52px;background:var(--navy-dark);color:var(--read-more);font-size:20px;line-height:52px}
.welcome{left:664px;top:437px;font-size:19px;font-weight:700;color:var(--ink)}
.welcome span{color:#6a9a10}
.para{font-size:11px;line-height:20px;color:var(--body-text);text-align:justify}
.man-servers{left:678px;top:588px;width:280px;height:120px;background:linear-gradient(90deg,#222 0,#333 75%,#eef1f4 76%)}
.included{left:74px;top:752px;font-size:19px;color:#13304d}
.checks{left:82px;top:855px;list-style:none;font-size:11.5px;color:var(--dark-text)}
.checks li{height:28px;display:flex;gap:12px}
.promo{left:261px;top:864px;width:381px;height:115px;border-radius:4px;background:linear-gradient(120deg,#a3c63a,#7ea81e);border:2px solid #8cb42a}
.gears{left:282px;top:885px;width:65px;height:65px;border-radius:50%;background:radial-gradient(#eee,#888)}
.ad{left:679px;top:760px;width:288px;height:240px;background:linear-gradient(#8cc23a 0,#8cc23a 13%,#123f7a 14%,#1f5da0 70%,#e9eef3 71%);border:1px solid #333}
.footer-links{left:59px;top:1040px;font-size:11.5px;color:var(--footer-text);display:flex;gap:8px}
.copy{left:59px;top:1068px;font-size:11.5px;color:var(--footer-text)}
.social{top:1049px;width:22px;height:22px;border-radius:50%;background:#fff}
</style>
</head>
<body>
<div class="page">
  <div class="abs logo">VLOMIK</div>
  <nav class="abs top-links"><span>SUPPORT</span><span>|</span><span>FAQ</span><span>|</span><span>HELP</span></nav>
  <div class="abs search">Search<svg width="14" height="14" viewBox="0 0 14 14"><circle cx="5.5" cy="5.5" r="4" fill="none" stroke="#999" stroke-width="2"/><line x1="8.5" y1="8.5" x2="13" y2="13" stroke="#999" stroke-width="2.5"/></svg></div>

  <div class="abs panel"></div>
  <nav class="abs nav">
    <a class="active" style="width:88px">HOME</a><a style="width:98px">ABOUT US</a><a style="width:124px">OUR SERVICES</a><a style="width:135px">HOSTING PLANS</a><a style="width:134px">RESELLER PLANS</a><a style="width:94px">SUPPORT</a><a style="width:114px">CONTACT US</a>
    <a style="width:163px;border:none"><svg width="16" height="16" viewBox="0 0 16 16"><circle cx="8" cy="5" r="4" fill="#fff"/><path d="M0 16c0-5 4-7 8-7s8 2 8 7z" fill="#fff"/></svg>MEMBER LOGIN</a>
  </nav>

  <section class="abs hero"></section>
  <h1 class="abs hero-title">Sedut perspiciatis unde omnisiste natus</h1>
  <div class="abs badge">From<b>$ 4.60</b></div>
  <ul class="abs bullets"><li>Nemo enim ipsam voluptatem quia</li><li>Ut enim ad minima veniam</li><li>Auis nostrum exercitationem ullam</li><li>Quis autem vel eum iure reprehenderit</li></ul>
  <div class="abs btn" style="left:470px">ORDER NOW</div>
  <div class="abs btn" style="left:581px">VIEW MORE</div>
  <div class="abs servers" role="img" aria-label="Photo of three rack servers"></div>

  <div class="abs plan" style="left:70px"><h2>STANDARD</h2><div class="card">
    <svg width="104" height="76"><polygon points="0,0 104,0 104,76 52,66 0,76" fill="var(--red)"/></svg>
    <div class="price">$150<i>per month</i></div>
    <ul><li>Nam eu libero nulla</li><li>Nullam ac metus</li><li>Donec rutrum interdum</li><li>Nunc at leo ut diam</li><li>Aenean pretium tellus</li></ul>
    <div class="more">READ MORE</div></div></div>
  <div class="abs plan" style="left:266px"><h2>ADVANCED</h2><div class="card">
    <svg width="104" height="76"><polygon points="0,0 104,0 104,76 52,66 0,76" fill="var(--green-dark)"/></svg>
    <div class="price">$150<i>per month</i></div>
    <ul><li>Nam eu libero nulla</li><li>Nullam ac metus</li><li>Donec rutrum interdum</li><li>Nunc at leo ut diam</li><li>Aenean pretium tellus</li></ul>
    <div class="more">READ MORE</div></div></div>
  <div class="abs plan" style="left:462px"><h2>BUSINESS</h2><div class="card">
    <svg width="104" height="76"><polygon points="0,0 104,0 104,76 52,66 0,76" fill="var(--blue)"/></svg>
    <div class="price">$150<i>per month</i></div>
    <ul><li>Nam eu libero nulla</li><li>Nullam ac metus</li><li>Donec rutrum interdum</li><li>Nunc at leo ut diam</li><li>Aenean pretium tellus</li></ul>
    <div class="more">READ MORE</div></div></div>

  <h2 class="abs welcome">WELCOME TO <span>VLOMIK</span></h2>
  <p class="abs para" style="left:666px;top:474px;width:312px">No one rejects, dislikes, or avoids pleasure itself, because it is pleasure, but because those who do not know how to pursue pleasure rationally encounter consequences that are extremely painful. Nor again is there anyone who loves or pursues or desires to obtain pain of itself.</p>
  <div class="abs man-servers" role="img" aria-label="Photo of a row of servers with a businessman leaning on them"></div>

  <h2 class="abs included">Your Hosting Included...</h2>
  <p class="abs para" style="left:76px;top:789px;width:580px;line-height:17.5px;color:var(--dark-text);text-align:left">No one rejects, dislikes, or avoids pleasure itself, because it is pleasure, but because those who do not know how to pursue pleasure rationally encounter consequences that are extremely painful. Nor again is there anyone who loves or pursues or desires to obtain pain of itself.</p>
  <ul class="abs checks">
    <li><svg width="14" height="12"><path d="M1 6l4 5 8-10" fill="none" stroke="#6ea81a" stroke-width="3"/></svg>Nam eu libero nulla</li>
    <li><svg width="14" height="12"><path d="M1 6l4 5 8-10" fill="none" stroke="#6ea81a" stroke-width="3"/></svg>Nullam ac metus</li>
    <li><svg width="14" height="12"><path d="M1 6l4 5 8-10" fill="none" stroke="#6ea81a" stroke-width="3"/></svg>Donec rutrum interdum</li>
    <li><svg width="14" height="12"><path d="M1 6l4 5 8-10" fill="none" stroke="#6ea81a" stroke-width="3"/></svg>Nunc at leo ut diam</li>
    <li><svg width="14" height="12"><path d="M1 6l4 5 8-10" fill="none" stroke="#6ea81a" stroke-width="3"/></svg>Aenean pretium tellus</li>
  </ul>
  <div class="abs promo"></div>
  <div class="abs gears" role="img" aria-label="Illustration of metal gears"></div>
  <h3 class="abs" style="left:367px;top:878px;color:#fff;font-size:15px;font-weight:400">At vero eos et accusamus et iusto</h3>
  <p class="abs para" style="left:367px;top:907px;width:263px;line-height:16px;color:#3a4a20">No one rejects, dislikes, or avoids pleasure itself, because it is pleasure.</p>
  <a class="abs" style="left:575px;top:947px;font-size:11px;color:#2a3a10;text-decoration:underline">View more</a>

  <aside class="abs ad" role="img" aria-label="Advertising banner for a file mirroring service"></aside>

  <nav class="abs footer-links"><span>Home</span>|<span>About Us</span>|<span>Our Services</span>|<span>Hosting Plans</span>|<span>Reseller Plans</span>|<span>Support</span>|<span>Contact Us</span>|<span>Member Login</span>|<span>Sitemap</span></nav>
  <p class="abs copy">Copyright © 2012 www.vlomik.example &nbsp; All rights reserved</p>
  <div class="abs social" style="left:912px"></div>
  <div class="abs social" style="left:939px"></div>
  <div class="abs social" style="left:966px"></div>
</div>
</body>
</html>
```